I would like a book cover for a new book I wrote called Tethered. Here is a brief description of the book.

In "Tethered," an evocative and courageous memoir, Carl Pettigrew draws a troubling parallel between the cult-like recruitment practices of the Lanternfield Fellowship and the manipulative tactics of sexual predators. From his early days in Boston to his tumultuous time in Bellevue, Nebraska, and beyond, the story is a raw and honest account of seeking authentic love and purpose amidst life's trials. It confronts themes of spiritual abuse, the pursuit of genuine connection, and the transformative power of facing one's past. This narrative offers a compelling look into the heart of a man who, despite many setbacks, discovers profound truths about love, redemption, and the human spirit.

```html
<!DOCTYPE html>
<html lang="en">
<head>
<meta charset="utf-8">
<title>Tethered — Cover Concepts</title>
<link rel="stylesheet" href="https://fonts.googleapis.com/css2?family=Zilla+Slab:wght@700&family=Crimson+Pro:ital,wght@1,400;1,600&display=swap">
<style>
  :root {
    --stage: #000000;
    --crimson: #9c1f1f;
    --gold: #d59a14;
    --paper: #ffffff;
    --ink: #000000;
    --note: #ffffff;
  }
  html, body {
    margin: 0;
    padding: 0;
    width: 1200px;
    height: 675px;
    overflow: hidden;
    background: var(--stage);
  }
  .board {
    position: relative;
    width: 1200px;
    height: 675px;
    background: var(--stage);
  }
  .cover {
    position: absolute;
    top: 79px;
    width: 323px;
    height: 516px;
  }
  .cover--crimson { left: 150px; }
  .cover--paper { left: 493px; }
  .cover svg { display: block; }
  .cover-title {
    font-family: "Zilla Slab", "Rockwell", serif;
    font-weight: 700;
    font-size: 40px;
  }
  .cover-label {
    font-family: "Crimson Pro", Georgia, serif;
    font-style: italic;
    font-size: 8px;
  }
  .date {
    position: absolute;
    left: 921px;
    top: 74px;
    margin: 0;
    color: var(--note);
    font-family: "Crimson Pro", Georgia, serif;
    font-style: italic;
    font-weight: 600;
    font-size: 16px;
  }
  .rationale {
    position: absolute;
    left: 839px;
    top: 407px;
    width: 230px;
    color: var(--note);
    font-family: "Crimson Pro", Georgia, serif;
    font-style: italic;
    font-size: 15.5px;
    line-height: 18.6px;
  }
  .rationale h2 {
    margin: 0 0 18.6px;
    font-size: 15.5px;
    font-weight: 400;
  }
  .rationale p { margin: 0; }
</style>
</head>
<body>
<main class="board">

  <section class="cover cover--crimson" aria-label="Cover option in crimson and gold">
    <svg width="323" height="516" viewBox="0 0 323 516" xmlns="http://www.w3.org/2000/svg">
      <rect width="323" height="516" fill="var(--crimson)"/>
      <g class="frame" stroke="var(--gold)" stroke-width="2" fill="none">
        <line x1="40" y1="15.5" x2="283" y2="15.5"/>
        <line x1="40" y1="503" x2="283" y2="503"/>
        <line x1="14" y1="50" x2="14" y2="464"/>
        <line x1="309" y1="50" x2="309" y2="464"/>
      </g>
      <g class="corner-ornaments" fill="var(--gold)" opacity="0.55">
        <rect role="img" aria-label="Floral corner ornament" x="10" y="12" width="40" height="40" rx="12"/>
        <rect role="img" aria-label="Floral corner ornament" x="273" y="12" width="40" height="40" rx="12"/>
        <rect role="img" aria-label="Floral corner ornament" x="10" y="464" width="40" height="40" rx="12"/>
        <rect role="img" aria-label="Floral corner ornament" x="273" y="464" width="40" height="40" rx="12"/>
      </g>
      <g class="cover-title" fill="var(--gold)" text-anchor="middle">
        <text x="161" y="162.5">T</text>
        <text x="29" y="200">T</text>
        <text x="62" y="200">E</text>
        <text x="95" y="200">T</text>
        <text x="128" y="200">H</text>
        <text x="161" y="200">E</text>
        <text x="194" y="200">R</text>
        <text x="227" y="200">E</text>
        <text x="260" y="200">D</text>
        <text x="161" y="237.5">T</text>
        <text x="161" y="275">H</text>
        <text x="161" y="312.5">E</text>
        <text x="161" y="350">R</text>
        <text x="161" y="387.5">E</text>
        <text x="161" y="425">D</text>
      </g>
      <text class="cover-label" x="161" y="495" fill="var(--gold)" text-anchor="middle">A Novel</text>
    </svg>
  </section>

  <section class="cover cover--paper" aria-label="Cover option in black and white">
    <svg width="323" height="516" viewBox="0 0 323 516" xmlns="http://www.w3.org/2000/svg">
      <rect width="323" height="516" fill="var(--paper)"/>
      <g class="frame" stroke="var(--ink)" stroke-width="2" fill="none">
        <line x1="40" y1="15.5" x2="283" y2="15.5"/>
        <line x1="40" y1="503" x2="283" y2="503"/>
        <line x1="14" y1="50" x2="14" y2="464"/>
        <line x1="309" y1="50" x2="309" y2="464"/>
      </g>
      <g class="corner-ornaments" fill="var(--ink)" opacity="0.55">
        <rect role="img" aria-label="Floral corner ornament" x="10" y="12" width="40" height="40" rx="12"/>
        <rect role="img" aria-label="Floral corner ornament" x="273" y="12" width="40" height="40" rx="12"/>
        <rect role="img" aria-label="Floral corner ornament" x="10" y="464" width="40" height="40" rx="12"/>
        <rect role="img" aria-label="Floral corner ornament" x="273" y="464" width="40" height="40" rx="12"/>
      </g>
      <g class="cover-title" fill="var(--ink)" text-anchor="middle">
        <text x="161" y="162.5">T</text>
        <text x="29" y="200">T</text>
        <text x="62" y="200">E</text>
        <text x="95" y="200">T</text>
        <text x="128" y="200">H</text>
        <text x="161" y="200">E</text>
        <text x="194" y="200">R</text>
        <text x="227" y="200">E</text>
        <text x="260" y="200">D</text>
        <text x="161" y="237.5">T</text>
        <text x="161" y="275">H</text>
        <text x="161" y="312.5">E</text>
        <text x="161" y="350">R</text>
        <text x="161" y="387.5">E</text>
        <text x="161" y="425">D</text>
      </g>
      <text class="cover-label" x="161" y="495" fill="var(--ink)" text-anchor="middle">A Novel</text>
    </svg>
  </section>

  <p class="date">02/11/2024</p>

  <article class="rationale">
    <h2>Tethered</h2>
    <p>I believe that it needs a strong cover but simple. This has a strong point and yet kept everything a mistery, it just shows the cross which will spark curiousity and that’s that, read it if you want to know more -type of thing .</p>
  </article>

</main>
</body>
</html>
```